Fennick Executive Search - New Business Card Design Project

We are an executive search firm called Fennick Executive Search based in the UK. We require a custom design for a business card. We're looking to convey a professional service to executives for executive search recruitment services. In terms of colours, we like dark blues and grays (maybe even silver incorporated somewhere if we go for a foiled type of card) but we're open to your artistic flare. See our current logo in attachments. We are totally open on design so long as the design is slick and professional.
Updates

Thanks for all your contributions of various designs. I have to say the quality of work has been amazing which is going to make our job quite difficult in the coming days on making a decision. Thanks to you all that have taken the time to submit designs thus far. We'll keep on reviewing and try to narrow down our selection as soon as possible.

Target Market(s)

Executive Search

Industry/Entity Type

Recruitment

Contact Information for Business Card

Fennick Executive Search,
Exclusively Sourcing & Hiring Senior Leaders
Gordon Pellbury, Managing Director,
07823 906417
0117 486 7132
gordon@fennickexecutive.co.uk
fennickexecutive.co.uk
58 Lindmoor Court, Hatherley Road, Bristol, BS32 9QJ

Font styles to use
Sans Serif
Other font styles liked:
• Roboto (which is used in our logo)

Requirements
Must have
• Our logo (It has a subtle fade on it from #02071d at top to #333649 at bottom)
• The logo can be on one side or both sides
• Must be elegant and professional
• We have 2nd slogan CONSULT | INSPIRE | INNOVATE | DELIVER which can be incorporated into the card
Nice to have
• Use of blues and grey colours
• Compatible with similar styling to our website fennickexecutive.co.uk
Should not have
• Must not be overly brash
• Must not contain cartoon characters

```html
<!DOCTYPE html>
<html lang="en">
<head>
<meta charset="utf-8">
<title>Fennick Executive Search – Business Card</title>
<link href="https://fonts.googleapis.com/css2?family=Montserrat:wght@400;500;700;800&display=swap" rel="stylesheet">
<style>
  :root {
    --backdrop: #d9dadd;
    --card-white: #fbfbfb;
    --navy-top: #1a2040;
    --navy-bottom: #0b0e1f;
    --ink: #141833;
    --ink-soft: #2a2d3d;
    --silver: #8b8e99;
    --silver-light: #a9abb3;
    --brand-light: #c9cbd3;
  }
  * { box-sizing: border-box; margin: 0; padding: 0; }
  html, body { width: 1200px; height: 900px; overflow: hidden; }
  body {
    background: var(--backdrop);
    font-family: "Montserrat", sans-serif;
    position: relative;
  }
  .card {
    position: absolute;
    top: 170px;
    width: 340px;
    height: 560px;
    border-radius: 26px;
    box-shadow: 0 18px 40px rgba(0,0,0,0.22);
  }
  .card--front { left: 200px; background: var(--card-white); }
  .card--back {
    left: 660px;
    background: radial-gradient(ellipse at 30% 20%, var(--navy-top), var(--navy-bottom) 75%);
  }
  .brand {
    position: absolute;
    top: 72px;
    left: 44px;
    font-weight: 700;
    font-size: 17px;
    line-height: 1.3;
    letter-spacing: 0.03em;
    text-transform: uppercase;
    color: var(--ink);
  }
  .card--back .brand { color: var(--brand-light); }

  .contact {
    position: absolute;
    left: 44px;
    top: 268px;
    color: var(--ink-soft);
  }
  .contact__name {
    font-weight: 800;
    font-size: 19px;
    letter-spacing: 0.03em;
    text-transform: uppercase;
    color: var(--ink);
  }
  .contact__role { font-size: 15px; margin-top: 3px; }
  .rule {
    width: 52px;
    height: 3px;
    background: var(--ink);
    margin: 16px 0 20px;
  }
  .contact__block { font-size: 14.5px; line-height: 1.5; }
  .contact__block + .contact__block { margin-top: 20px; }

  .tagline {
    position: absolute;
    left: 44px;
    bottom: 74px;
    color: var(--silver);
    font-size: 15px;
    line-height: 1.35;
  }
  .tagline__firm { font-weight: 700; color: var(--silver-light); }
  .tagline .rule { background: var(--silver); margin: 16px 0 14px; }
  .tagline__web { font-size: 15px; }
  .tagline__web strong { font-weight: 700; }
</style>
</head>
<body>
  <section class="card card--front" aria-label="Business card front">
    <p class="brand">Fennick<br>Executive Search</p>
    <div class="contact">
      <h1 class="contact__name">Gordon Pellbury</h1>
      <p class="contact__role">Managing Director</p>
      <div class="rule"></div>
      <p class="contact__block">58 Lindmoor Court, Hatherley Road,<br>Bristol, BS32 9QJ</p>
      <p class="contact__block">07823 906417<br>0117 486 7132<br>gordon@fennickexecutive.co.uk<br>fennickexecutive.co.uk</p>
    </div>
  </section>

  <section class="card card--back" aria-label="Business card back">
    <p class="brand">Fennick<br>Executive Search</p>
    <div class="tagline">
      <p class="tagline__firm">Fennick Executive Search</p>
      <p>Exclusively Sourcing &amp;<br>Hiring Senior Leaders</p>
      <div class="rule"></div>
      <p class="tagline__web"><strong>fennickexecutive</strong>.co.uk</p>
    </div>
  </section>
</body>
</html>
```